School District In Need of Powerful Presentation

Create a modern PPT design template -- standard and widescreen -- for the Pell County Schools school district inspired by its logo. The presentation should be a modern projection of 21st education that excites the people who view it. The school district is located in a rural farming community with a view of the rocky mountains to its west (check out this picture www.campsiteatmarblefork.example/AnimatedImages/HomeGallery/000MountainScene.jpg). People in this community want quality education for their children with opportunities for them to be successful after they graduate.

Target Market(s)

The Harbrook and Denning communities in Northern Colorado

Industry/Entity Type

Education

Font styles to use
Sans Serif

Colors
ec1f27
3176b5
acd036
fece3e
f78f20

Requirements
Must have
• The name of the school district:
• Pell County School District RU-8K Harbrook-Denning
• Website address: www.pellru8k.example/
• Email: listen@pellru8k.example
Nice to have
• A couple of color options including their current color scheme: red, gold, black
• Placeholder for pictures of students and teachers
Should not have
• Please do not use the full logo in it's current for, but you may use elements of the logo.

```html
<!DOCTYPE html>
<html lang="en">
<head>
<meta charset="utf-8">
<title>Our Students – Pell County Schools</title>
<link href="https://fonts.googleapis.com/css2?family=Trocchi&display=swap" rel="stylesheet">
<style>
:root{
  --red:#ec1f27;
  --red-deep:#d81e2a;
  --gold:#fece3e;
  --green:#acd036;
  --ink:#111111;
  --white:#ffffff;
}
*{margin:0;padding:0;box-sizing:border-box}
html,body{width:1200px;height:769px;overflow:hidden}
body{font-family:"Trocchi",Georgia,serif;background:var(--red);font-variant-numeric:lining-nums}
.slide{position:relative;width:1200px;height:769px;overflow:hidden;
  background:linear-gradient(135deg,#e3333a 0%,#e32530 45%,#d91f2b 100%)}
.slide__backdrop{position:absolute;inset:106px 0 33px 0;
  background:radial-gradient(ellipse at 35% 35%,rgba(255,140,120,.3),transparent 55%),
  radial-gradient(ellipse at 75% 60%,rgba(120,0,10,.22),transparent 60%)}
.header{position:absolute;left:0;top:17px;width:1200px;height:89px;background:var(--gold);
  display:flex;align-items:center;justify-content:space-between;padding:0 16px}
.header__title{font-size:39px;color:var(--ink);letter-spacing:.5px;font-weight:400;
  text-shadow:1px 1px 0 rgba(255,255,255,.45)}
.brand{display:flex;align-items:center;gap:8px}
.brand__dot{width:18px;height:18px;border-radius:50%;background:var(--red-deep)}
.brand__name{font-size:15px;color:var(--ink)}
.card{position:absolute;top:172px;width:300px;text-align:center;color:var(--white)}
.card--one{left:54px}.card--two{left:436px}.card--three{left:833px}
.card__photo{display:block;margin:0 auto;width:232px;height:232px;border-radius:50%;
  border:6px solid var(--gold);box-shadow:0 0 0 2px rgba(255,255,255,.55)}
.card__photo--one{background:linear-gradient(160deg,#d9e8f0,#6d95b5 55%,#9a6a4a)}
.card__photo--two{background:linear-gradient(160deg,#d8c9b3,#b9826a 50%,#c4262a)}
.card__photo--three{background:linear-gradient(160deg,#f0eee8,#c59a7f 50%,#3c8a3c)}
.card__title{font-weight:400;font-size:24px;margin-top:22px;line-height:30px}
.card__text{font-size:14.6px;line-height:25.6px;margin:6px auto 0;width:286px}
.footer{position:absolute;left:0;bottom:0;width:1200px;height:33px;background:var(--green);
  display:flex;align-items:center;justify-content:space-between;padding:0 8px 0 8px;
  font-size:13.5px;color:var(--ink)}
</style>
</head>
<body>
<main class="slide">
  <div class="slide__backdrop" role="img" aria-label="Faded classroom photo of smiling students"></div>
  <header class="header">
    <h1 class="header__title">OUR STUDENTS</h1>
    <div class="brand"><span class="brand__dot"></span><span class="brand__name">Pell County Schools</span></div>
  </header>
  <section class="cards">
    <article class="card card--one">
      <div class="card__photo card__photo--one" role="img" aria-label="Students raising hands in a classroom"></div>
      <h2 class="card__title">IMAGE TITLE HERE</h2>
      <p class="card__text">Lorem Ipsum is simply dummy text of the printing and typesetting industry. Lorem Ipsum has been the industry's standard dummy text ever since the 1500s, when an unknown printer took a galley of type and scrambled it to make a type specimen book. It has survived not only five centuries,</p>
    </article>
    <article class="card card--two">
      <div class="card__photo card__photo--two" role="img" aria-label="Smiling young student in a classroom"></div>
      <h2 class="card__title">IMAGE TITLE HERE</h2>
      <p class="card__text">Lorem Ipsum is simply dummy text of the printing and typesetting industry. Lorem Ipsum has been the industry's standard dummy text ever since the 1500s, when an unknown printer took a galley of type and scrambled it to make a type specimen book. It has survived not only five centuries,</p>
    </article>
    <article class="card card--three">
      <div class="card__photo card__photo--three" role="img" aria-label="Row of students listening in class"></div>
      <h2 class="card__title">IMAGE TITLE HERE</h2>
      <p class="card__text">Lorem Ipsum is simply dummy text of the printing and typesetting industry. Lorem Ipsum has been the industry's standard dummy text ever since the 1500s, when an unknown printer took a galley of type and scrambled it to make a type specimen book. It has survived not only five centuries,</p>
    </article>
  </section>
  <footer class="footer">
    <span class="footer__copyright">COPYRIGHT TEXT HERE</span>
    <span class="footer__page">PAGE : 01</span>
  </footer>
</main>
</body>
</html>
```